Business Card for New Business

Please design a business card using our logo and font files. This is only one card for one person, as listed in details section.

Contact Information for Business Card

Dale Vornhuser

Phone 240.815.3926
Cell 703.461.8075
Email dale@morlenbay.com

www.morlenbay.com

Address
31800 Pinecrest Lane #412
Elmridge, MD 20934

Font styles to use
Sans Serif

Requirements
Must have
• Information listed in detail section. Must be standard card size.

```html
<!DOCTYPE html>
<html lang="en">
<head>
<meta charset="utf-8">
<title>Morlenbay Productions – Business Card</title>
<link href="https://fonts.googleapis.com/css2?family=Roboto:ital,wght@0,300;0,400;1,400;1,700&display=swap" rel="stylesheet">
<style>
  :root {
    --page: #e4e4e4;
    --card-dark: #1f1f1f;
    --card-light: #ffffff;
    --accent: #e0561e;
    --text-light: #f2f2f2;
  }
  * { box-sizing: border-box; margin: 0; padding: 0; }
  html, body { width: 1200px; height: 900px; overflow: hidden; }
  body {
    background: var(--page);
    font-family: "Roboto", Arial, sans-serif;
    position: relative;
  }
  .card {
    position: absolute;
    width: 560px;
    height: 320px;
    left: 320px;
    overflow: hidden;
    box-shadow: 0 6px 18px rgba(0,0,0,0.18);
  }
  .card-back { top: 95px; background: var(--card-dark); }
  .card-front { top: 475px; background: var(--card-dark); }

  .brand {
    position: absolute;
    display: flex;
    align-items: center;
    gap: 12px;
    color: var(--accent);
    font-weight: 300;
  }
  .brand-mark {
    border-radius: 50%;
    background: var(--accent);
    flex: none;
  }
  .brand-name { line-height: 1; }
  .brand-name .line-1 { display: block; letter-spacing: 1px; }
  .brand-name .line-2 { display: block; text-transform: uppercase; }

  .card-back .brand { left: 0; right: 0; top: 108px; justify-content: center; }
  .card-back .brand-mark { width: 50px; height: 50px; }
  .card-back .brand-name .line-1 { font-size: 56px; }
  .card-back .brand-name .line-2 { font-size: 19px; letter-spacing: 11.5px; margin-top: 8px; }

  .front-shape { position: absolute; inset: 0; }
  .card-front .brand { left: 336px; top: 136px; gap: 8px; }
  .card-front .brand-mark { width: 26px; height: 26px; }
  .card-front .brand-name .line-1 { font-size: 30px; }
  .card-front .brand-name .line-2 { font-size: 10.5px; letter-spacing: 5.6px; margin-top: 5px; }

  .holder { position: absolute; left: 26px; top: 22px; }
  .holder-name {
    color: var(--accent);
    font-weight: 700;
    font-style: italic;
    font-size: 16px;
  }
  .holder-title {
    color: var(--text-light);
    font-style: italic;
    font-size: 11.5px;
    margin-top: 2px;
  }

  .address {
    position: absolute;
    left: 26px;
    top: 150px;
    color: var(--text-light);
    font-size: 12.5px;
    line-height: 17px;
    font-style: normal;
  }
  .contacts {
    position: absolute;
    left: 26px;
    top: 196px;
    list-style: none;
    color: var(--text-light);
    font-size: 12.5px;
    line-height: 19px;
  }
  .contacts li { display: flex; align-items: center; gap: 7px; }
  .contacts svg { width: 10px; height: 10px; fill: var(--accent); flex: none; }
</style>
</head>
<body>

<section class="card card-back">
  <div class="brand">
    <span class="brand-mark"></span>
    <span class="brand-name">
      <span class="line-1">morlenbay</span>
      <span class="line-2">productions</span>
    </span>
  </div>
</section>

<section class="card card-front">
  <svg class="front-shape" viewBox="0 0 560 320" width="560" height="320" aria-hidden="true">
    <path d="M372 0 Q248 160 352 320 L560 320 L560 0 Z" fill="var(--card-light)"/>
    <path d="M362 0 Q236 162 340 320" fill="none" stroke="var(--accent)" stroke-width="11"/>
    <path d="M348 0 Q222 165 330 320" fill="none" stroke="var(--accent)" stroke-width="2.5"/>
    <path d="M369 0 Q245 160 349 320" fill="none" stroke="var(--card-light)" stroke-width="2"/>
  </svg>

  <div class="holder">
    <p class="holder-name">Dale Vornhuser</p>
    <p class="holder-title">President</p>
  </div>

  <address class="address">
    31800 Pinecrest Lane #412<br>
    Elmridge, MD 20934
  </address>

  <ul class="contacts">
    <li>
      <svg viewBox="0 0 10 10"><path d="M2 0.5 L3.6 2.6 L2.8 3.6 Q4 6 6.4 7.2 L7.4 6.4 L9.5 8 L8.4 9.5 Q4 9 0.5 1.6 Z"/></svg>
      240.815.3926
    </li>
    <li>
      <svg viewBox="0 0 10 10"><path d="M2.5 0 H7.5 V10 H2.5 Z M3.4 1.2 V7.8 H6.6 V1.2 Z"/></svg>
      703.461.8075
    </li>
    <li>
      <svg viewBox="0 0 10 10"><path d="M0 2 H10 V8.5 H0 Z M0.8 2.6 L5 5.8 L9.2 2.6 Z"/></svg>
      dale@morlenbay.com
    </li>
    <li>
      <svg viewBox="0 0 10 10"><circle cx="5" cy="5" r="4.3" fill="none" stroke="var(--accent)" stroke-width="1.2"/><path d="M0.8 5 H9.2 M5 0.8 Q2.4 5 5 9.2 Q7.6 5 5 0.8" fill="none" stroke="var(--accent)" stroke-width="0.9"/></svg>
      www.morlenbay.com
    </li>
  </ul>

  <div class="brand">
    <span class="brand-mark"></span>
    <span class="brand-name">
      <span class="line-1">morlenbay</span>
      <span class="line-2">productions</span>
    </span>
  </div>
</section>

</body>
</html>
```